Postcard for our major fundraising event - LiftingSTAR2018

Bright Meadow KIDS Camp (BMK) and Youth Trail Pathway Camp (YTPC) are ministries of Larkfield Gospel Church that serve Ventura County children of abuse, abandonment and neglect living in foster care. We are looking for a postcard design to promote our single largest fundraising event of the year, NurturingSTAR2018, to raise awareness and support for children of abuse. NurturingSTAR is a dinner banquet on at an exclusive outdoor venue, "Willow Hollow" with a rustic, ranch feel and with spectacular panoramic views of the City of Camarillo. The event will include music, refreshments, appetizers, a Santa Maria-style barbeque (BBQ), coffee and dessert, testimonials from camp, prize drawings, an opportunity to partner with BMK and YTPC, and time to socialize before and after.
Updates

I have just uploaded text copy to help designers come closer to what we are looking for. Thank you very much for your interest! -Dale

Target Market(s)

People from both within and from outside our sponsoring church who have a heart for hurting children and who are willing and able to financially support our camping (BMK & YTPC) ministries.

Industry/Entity Type

Church

Font styles to use
Serif
Decorative
Script

Requirements
Must have
• Name: NurturingSTAR2018... raising awareness and support for children of abuse
• Date: Thursday, May 24, 2018, 6:30-8:00 pm
• Place: Willow Hollow at Marlowe Ranch, 7100 Quillan Road, Somis, California.
• Cost: $30 per person
• Tickets: Available at Ticketmill.example
• Front side should include the elements of the event (although not necessarily bulleted like below):
• • Social hour
• • Music
• • Hors d’eourves
• • Refreshments
• • Santa Maria-style BBQ dinner
• • Coffee & dessert
• • Prize drawings
• • Stories from camp
• See attachment for suggested copy for back side.
• BMK and YTPC logos should be included on the postcard. I’ve uploaded a variety of photos for the designer to choose from; they do not necessarily all have to be included. There are also lots more pics available on our Gatherbook (Bright Meadow KIDS of Ventura).
• The front-side of the postcard can be entirely images and text. The back-side of the post card should include our return address at the top left ("BMK/YTPC of Larkfield Gospel Church, 820 Fernbrook Lane, Ventura, CA 93003") and should leave at least the right half of the postcard clear for addressing and postage.
• BMK colors are purple (Pantone 267) and red (Pantone 186). YTPC colors are green and yellow.
Nice to have
• A selection of camp photos large enough to easily view, but no so many that they are too small to identify. And, perhaps, a design element that evokes a rustic, outdoors, western, ranch feel, but not so much that it seems that we are promoting a country hoedown.
Should not have
• Anything sexual or sensual, related to alcoholic beverages, gambling, guns, or anything negative.

```html
<!DOCTYPE html>
<html lang="en">
<head>
<meta charset="utf-8">
<title>NurturingSTAR 2018 Postcard</title>
<link href="https://fonts.googleapis.com/css2?family=Bungee&family=Dancing+Script:wght@600&family=Open+Sans:wght@400;600;700;800&display=swap" rel="stylesheet">
<style>
:root{
  --backdrop:#d9dadb;
  --navy:#0c1430;
  --navy-2:#1a2450;
  --red:#e3243b;
  --purple:#5b2c86;
  --orange:#f47a20;
  --yellow:#f6c51b;
  --green:#2f9a48;
  --pink:#ec3a74;
  --cyan:#2bb3e3;
  --ink:#2a2a2a;
  --white:#ffffff;
}
*{box-sizing:border-box;margin:0;padding:0}
html,body{width:900px;height:1200px;overflow:hidden}
body{background:var(--backdrop);font-family:"Open Sans",Arial,sans-serif;position:relative}
.side-label{position:absolute;left:0;width:900px;text-align:center;font-size:20px;color:#555}
.card{position:absolute;left:66px;width:780px;box-shadow:0 6px 16px rgba(0,0,0,.3)}

/* front */
.front{top:18px;height:540px;background:radial-gradient(circle at 75% 30%,var(--navy-2),var(--navy) 70%);overflow:hidden}
.front .collage{position:absolute;left:-60px;top:-20px;width:520px;height:520px;border-radius:50%;
  background:radial-gradient(circle at 45% 45%,#a7b6a0,#6f8a86 45%,#3a4d6a 75%,#1a2450);border:4px solid rgba(255,255,255,.5)}
.front .intro{position:absolute;left:440px;top:22px;width:320px;text-align:center}
.intro .camp-a{color:var(--red);font-weight:800;font-size:22px;line-height:1.1}
.intro .camp-b{color:var(--yellow);font-weight:800;font-size:21px;line-height:1.15}
.intro .church{color:var(--white);font-weight:700;font-size:14px;margin-top:4px}
.intro .invite{color:var(--white);font-size:13px;font-style:italic;margin-top:6px}
.event-title{font-family:"Bungee",Impact,sans-serif;line-height:.95}
.event-title .w1{display:block;color:var(--orange)}
.event-title .w2{color:var(--pink)}
.event-title .year{display:inline-block;font-size:.42em;line-height:1;vertical-align:top;color:var(--cyan);margin-left:6px}
.front .event-title{position:absolute;left:440px;top:170px;width:330px;font-size:52px}
.front .event-title .w2{font-size:84px}
.tagline{font-family:"Dancing Script",cursive;color:var(--white)}
.front .tagline{position:absolute;left:440px;top:330px;font-size:20px}
.features{position:absolute;left:445px;top:380px;width:320px;display:grid;grid-template-columns:1fr 1fr;gap:9px 12px;list-style:none;color:var(--white);font-size:14px}
.features li::before{content:"";display:inline-block;width:8px;height:8px;background:var(--orange);border-radius:50%;margin-right:8px;vertical-align:middle}

/* back */
.back{top:630px;height:510px;background:var(--white)}
.back .info{position:absolute;left:26px;top:18px;width:360px;text-align:center;color:var(--ink)}
.brands{display:flex;justify-content:center;align-items:center;gap:22px}
.brand{font-weight:800;font-size:17px;color:var(--purple);line-height:1.05}
.brand-b{display:flex;align-items:center;gap:6px;font-weight:800;font-size:17px;color:var(--green)}
.brand-b .dot{width:24px;height:24px;border-radius:50%;background:var(--green)}
.info .church{font-size:12px;font-weight:600;margin-top:4px}
.info .invite{font-size:12px;font-style:italic}
.back .event-title{font-size:34px;margin-top:6px}
.back .event-title .w2{font-size:50px}
.back .tagline{color:var(--purple);font-size:16px}
.venue-pre{font-size:11px;margin-top:6px;font-style:italic}
.venue{color:var(--red);font-weight:800;font-size:15px;text-transform:uppercase}
.address{font-size:12px}
.date-band{background:var(--green);color:var(--white);font-weight:700;font-size:14px;padding:5px;margin:8px 20px 0}
.tickets{border:1px solid var(--green);font-size:12px;padding:5px;margin:8px 30px 0}
.tickets b{color:var(--red);font-size:15px}
.contact{font-size:10.5px;margin-top:10px;line-height:1.45}
.contact .head{font-weight:700}
.back .divider{position:absolute;left:408px;top:40px;width:1px;height:430px;background:#ccc}
.stamp{position:absolute;right:26px;top:22px;width:70px;height:84px;border:1px dashed #aaa}
.address-lines{position:absolute;left:450px;top:250px;width:300px}
.address-lines span{display:block;height:1px;background:#bbb;margin-bottom:38px}
.return{position:absolute;display:none}
</style>
</head>
<body>
<section class="card front">
  <div class="collage" role="img" aria-label="Circular collage of camp photos: children and counselors outdoors"></div>
  <div class="intro">
    <p class="camp-a">Bright Meadow KIDS Camp &amp;</p>
    <p class="camp-b">Youth Trail Pathway Camp</p>
    <p class="church">of Larkfield Gospel Church</p>
    <p class="invite">invites you to join us for</p>
  </div>
  <h1 class="event-title"><span class="w1">NURTURING</span><span class="w2">STAR</span><span class="year">20<br>18</span></h1>
  <p class="tagline">raising awareness &amp; support for children of abuse</p>
  <ul class="features">
    <li>Social hour</li><li>Santa Maria-style BBQ dinner</li>
    <li>Music</li><li>Coffee &amp; dessert</li>
    <li>Hors d’oeuvres</li><li>Prize drawings</li>
    <li>Refreshments</li><li>Stories from camp</li>
  </ul>
</section>
<p class="side-label" style="top:570px">Front</p>

<section class="card back">
  <div class="info">
    <div class="brands">
      <span class="brand">Bright Meadow<br>KIDS</span>
      <span class="brand-b"><span class="dot"></span>YTPC</span>
    </div>
    <p class="church">of Larkfield Gospel Church</p>
    <p class="invite">invite you to join us at our</p>
    <h2 class="event-title"><span class="w1">NURTURING</span><span class="w2">STAR</span><span class="year">20<br>18</span></h2>
    <p class="tagline">raising awareness &amp; support for children of abuse</p>
    <p class="venue-pre">at the exclusive</p>
    <p class="venue">Willow Hollow at Marlowe Ranch</p>
    <p class="address">7100 Quillan Road, Somis, CA</p>
    <p class="date-band">on Thursday, May 24, 2018 &nbsp;6:30-8:00pm</p>
    <p class="tickets">Tickets <b>$30</b> per person. Available at Ticketmill.example<br>All proceeds to benefit BMK &amp; YTPC serving children of abuse ages 7-16</p>
    <div class="contact">
      <p class="head">For more information:</p>
      <p>BMK: Director Dale Penner (805) 555-0142 | bmk@larkfield.example</p>
      <p>YTPC: Director Nora Wills (805) 555-0187 | ytpc@larkfield.example</p>
    </div>
  </div>
  <div class="divider"></div>
  <div class="stamp"></div>
  <div class="address-lines"><span></span><span></span><span></span><span></span></div>
</section>
<p class="side-label" style="top:1160px">Back</p>
</body>
</html>
```